Need a clean & modern homepage for an education site + opportunity for longer term work

Thanks for viewing our project. We are excited about this new website and we hope that we might build a relationship with designers as we work on this project. I provided quite a few details and requirements to help you more quickly create a design that meets our needs.
Who we are:
We are a website that discusses the importance of college accreditation and provides a directory of college programs.
What we need:
A homepage that meets the below requirements and is inspired by the examples provided
Definition of accredited:
ac·cred·it·ed [uh-kred-i-tid] adj.
1. officially recognized as meeting the essential requirements, as of academic excellence: accredited schools.
2. provided with official credentials, as by a government: an accredited diplomatic representative.
3. accepted as authoritative: an accredited theory.
Overall look and feel for the homepage:
- Clean, simple and modern
- Limited (or zero) pictures
- Utilize color blocks with text
- A trend seems to be longer vertical length homepages with lots of whitespace. I generally like this trend as long as the page is not way to tall.
Inspirations: Sites that have a similar look and feel to what I need.
http://plinvar.org/
http://www.tumbrelstat.com/colleges/harrowgate-university/
http://quietmarble.org/
http://www.vellichorstaffing.com/
http://www.plonk.com/
http://sketches.zimvo.com/
Items to be included on the homepage. Details below on each item.
- Top navigation
- Logo: Please leave a blank area for a logo. The logo has not been designed.
- Simple graphic/color block at the top that highlights a definition of “CREDENTIA” – the definition should be formatted like it is being copy/pasted from a dictionary.
- Space for a video and small (50 word) written description of the video. You can use placeholder text.
- One section with 3 Paragraphs of content (each paragraph around 100 words) with a header at the top. You can use placeholder text but please create the formatting. At the end of the 3 paragraphs please have a “Read More” Note this shouldn't be 3 separate paragraphs with three read mores - it is 3 paragraphs with one read more at the end.
- An area with the header “Search Colleges by State” that has anchor text links to all 50 states.
Top navigation:
- Home
- States – with a subnav dropdown that includes all 50 US states.
- Programs – with a subnav dropdown that includes program titles (list below)
- Degrees - with a subnav dropdown that includes 5 degree levels (list below)
- Accreditation – no subnav
- Rankings – no subnav
- Resources – no subnav
Footer
- Link to about us, privacy, and a copyright www.url.com
Programs List for sub navigation
Accounting
Art
Bible
Business
Criminal Justice
Design
Engineering
English
Law
LPN to RN
Management
Math
MBA
MPH
Medical Assisting
Military
Nursing
Occupational Therapy
Paralegal
Psychology
Pharmacy
RN to BSN
Radiology
Social Work
Sonography
Degrees list for sub navigation
Certificate
Associate
Bachelors
Masters
PhD
Thanks so much - looking forward to working with you!

```html
<!DOCTYPE html>
<html lang="en">
<head>
<meta charset="utf-8">
<title>Credentia</title>
<link href="https://fonts.googleapis.com/css2?family=Arimo:wght@400;700&family=PT+Sans:wght@400;700&display=swap" rel="stylesheet">
<style>
:root{
  --page:#ebe9e5;
  --white:#ffffff;
  --blue:#1b4a7a;
  --blue-edge:#2d5d8e;
  --green:#6a9a00;
  --green-bright:#8cc300;
  --btn-top:#86b624;
  --btn-bottom:#5a8a0c;
  --logo:#666666;
  --text:#9a9a9a;
  --heading:#333333;
  --menu-text:#555555;
  --line:#c9c6c0;
  --border:#d6d4d0;
}
*{margin:0;padding:0;box-sizing:border-box}
html,body{width:1200px;height:981px;overflow:hidden}
body{background:var(--page);font-family:"Arimo",Arial,sans-serif;position:relative}
.site-name{position:absolute;left:120px;top:40px;font:700 38px/1 "Arimo",Arial,sans-serif;color:var(--logo);letter-spacing:0.5px}

.state-search{position:absolute;left:577px;top:82px;width:509px;height:42px;background:var(--white);border:1px solid var(--border);border-radius:3px}
.state-search label{position:absolute;left:9px;top:15px;font-size:11.6px;color:#666}
.state-search .field{position:absolute;left:195px;top:8px;width:230px;height:26px;border:1px solid #c8c8c8;border-radius:3px;background:var(--white)}
.btn{display:block;background:linear-gradient(var(--btn-top),var(--btn-bottom));color:var(--white);border:1px solid #4c7a06;border-radius:3px;font:700 12px/1 "Arimo",Arial,sans-serif;text-align:center;text-shadow:0 1px 0 rgba(0,0,0,.35)}
.state-search .btn{position:absolute;left:397px;top:8px;width:100px;height:26px;line-height:24px;font-size:10px;letter-spacing:1px}

.hero{position:absolute;left:0;top:155px;width:1200px;height:300px;background:var(--blue);border-top:5px solid var(--blue-edge);border-bottom:7px solid var(--blue-edge)}
.definition{position:absolute;left:0;top:0;width:1160px;text-align:center;font-family:"PT Sans",Tahoma,sans-serif;font-weight:700;color:var(--white)}
.definition p{position:absolute;left:0;width:100%;white-space:nowrap}
.definition .accent{color:var(--green-bright)}
.d1{top:31px;font-size:22px;letter-spacing:1.1px}
.d2{top:57px;font-size:27px;letter-spacing:1.7px}
.d3{top:122px;font-size:31px;letter-spacing:1.2px}
.d4{top:161px;font-size:21px;letter-spacing:1.2px}
.d5{top:222px;font-size:25px;letter-spacing:1.8px}
.d6{top:243px;font-size:31px;letter-spacing:1.7px}
.rule{position:absolute;left:232px;width:699px;height:1px;background:#c8d3df}
.rule.r1{top:108px}.rule.r2{top:204px}
.slide-arrow{position:absolute;top:111px;width:44px;height:44px}
.slide-arrow.prev{left:111px}.slide-arrow.next{left:1045px}

.main-nav{position:absolute;left:110px;top:123px;width:980px;height:42px;background:linear-gradient(#ffffff,#f4f4f4);border:1px solid var(--border);border-radius:4px;display:flex}
.main-nav a{height:40px;line-height:42px;text-align:center;color:var(--green);font-weight:700;font-size:13.5px;text-decoration:none;border-right:1px solid #e3e3e3}
.main-nav a:last-child{border-right:none}

.submenu{position:absolute;top:164px;background:var(--page);box-shadow:0 1px 4px rgba(0,0,0,.35);padding:4px 2px 2px;list-style:none}
.submenu li{height:20px;line-height:20px;padding-left:19px;font-size:10.5px;color:var(--menu-text);border-bottom:1px solid var(--line)}
.submenu li:last-child{border-bottom:none}
.programs-menu{left:336px;width:215px}
.degrees-menu{left:483px;width:214px}

.footer-band{position:absolute;left:0;top:912px;width:1200px;height:69px;background:var(--blue)}
.content{position:absolute;left:110px;top:476px;width:980px;height:455px;background:var(--white);border:1px solid var(--border);border-radius:4px}
.content h2{position:absolute;font:700 18px/1 "Arimo",Arial,sans-serif;color:var(--heading);letter-spacing:.5px}
.article h2{left:29px;top:24px}
.video h2{left:668px;top:24px}
.article p{position:absolute;left:29px;width:571px;font-size:12px;line-height:16.9px;color:var(--text);text-align:justify}
.article .p1{top:59px}.article .p2{top:179px}.article .p3{top:299px}
.content .btn{position:absolute;top:405px;width:96px;height:24px;line-height:22px;font-size:12px}
.article .btn{left:492px}
.divider{position:absolute;left:629px;top:17px;height:288px;border-left:2px dotted #dcdcdc}
.video-frame{position:absolute;left:668px;top:62px;width:281px;height:197px;border:1px solid var(--border);padding:2px;background:var(--white)}
.video-screen{width:100%;height:100%;background:radial-gradient(circle at 50% 45%,#555 0%,#2a2a2a 55%,#161616 100%);position:relative}
.video-screen svg{position:absolute;left:106px;top:65px}
.video p{position:absolute;left:667px;top:271px;width:284px;font-size:12px;line-height:16.9px;color:var(--text);text-align:justify}
.video .btn{left:853px}

.footer-links{position:absolute;left:141px;top:951px;font-size:10.4px;color:var(--white)}
.footer-links a{color:var(--white);text-decoration:none}
.footer-links span{margin:0 5px}
.copyright{position:absolute;right:139px;top:951px;font-size:10.2px;color:var(--white)}
</style>
</head>
<body>

<div class="site-name">CREDENTIA</div>

<form class="state-search">
  <label>SEARCH COLLEGES BY STATE :</label>
  <span class="field"></span>
  <span class="btn">SEARCH</span>
</form>

<section class="hero">
  <div class="definition">
    <p class="d1">OFFICIALLY RECOGNIZED AS MEETING THE ESSENTIAL REQUIREMENTS,</p>
    <p class="d2 accent">AS OF ACADEMIC EXCELLENCE: ACCREDITED SCHOOLS.</p>
    <p class="d3">PROVIDED WITH OFFICIAL CREDENTIALS,</p>
    <p class="d4">AS BY A GOVERNMENT: <span class="accent">AN ACCREDITED DIPLOMATIC REPRESENTATIVE.</span></p>
    <p class="d5">ACCEPTED AS AUTHORITATIVE:</p>
    <p class="d6 accent">AN ACCREDITED THEORY.</p>
  </div>
  <div class="rule r1"></div>
  <div class="rule r2"></div>
  <svg class="slide-arrow prev" viewBox="0 0 44 44"><circle cx="22" cy="22" r="21" fill="#173c63"/><circle cx="22" cy="22" r="18" fill="#fff" stroke="#d8d8d8"/><path d="M26 14 L17 22 L26 30" fill="none" stroke="#6a9a00" stroke-width="5"/></svg>
  <svg class="slide-arrow next" viewBox="0 0 44 44"><circle cx="22" cy="22" r="21" fill="#173c63"/><circle cx="22" cy="22" r="18" fill="#fff" stroke="#d8d8d8"/><path d="M18 14 L27 22 L18 30" fill="none" stroke="#6a9a00" stroke-width="5"/></svg>
</section>

<nav class="main-nav">
  <a style="width:111px">HOME</a>
  <a style="width:115px">STATES</a>
  <a style="width:146px">PROGRAMS</a>
  <a style="width:131px">DEGREES</a>
  <a style="width:182px">ACCREDITATION</a>
  <a style="width:141px">RANKINGS</a>
  <a style="width:152px">RESOURCES</a>
</nav>

<div class="footer-band"></div>

<main class="content">
  <section class="article">
    <h2>VIDEO</h2>
    <p class="p1">Lorem Ipsum is simply dummy text of the printing and typesetting industry. Lorem Ipsum has been the industry's standard dummy text ever since the 1500s, when an unknown printer took a galley of type and scrambled it to make a type specimen book. It has survived not only five centuries, but also the leap into electronic typesetting, remaining essentially unchanged. It was popularised in the 1960s with the release of Marvane sheets containing Lorem Ipsum passages, and more recently with desktop publishing software like Quillo PageSetter including versions of Lorem Ipsum.</p>
    <p class="p2">Lorem Ipsum is simply dummy text of the printing and typesetting industry. Lorem Ipsum has been the industry's standard dummy text ever since the 1500s, when an unknown printer took a galley of type and scrambled it to make a type specimen book. It has survived not only five centuries, but also the leap into electronic typesetting, remaining essentially unchanged. It was popularised in the 1960s with the release of Marvane sheets containing Lorem Ipsum passages, and more recently with desktop publishing software like Quillo PageSetter including versions of Lorem Ipsum.</p>
    <p class="p3">Lorem Ipsum is simply dummy text of the printing and typesetting industry. Lorem Ipsum has been the industry's standard dummy text ever since the 1500s, when an unknown printer took a galley of type and scrambled it to make a type specimen book. It has survived not only five centuries, but also the leap into electronic typesetting, remaining essentially unchanged. It was popularised in the 1960s with the release of Marvane sheets containing Lorem Ipsum passages, and more recently with desktop publishing software like Quillo PageSetter including versions of Lorem Ipsum.</p>
    <a class="btn">READ MORE</a>
  </section>
  <div class="divider"></div>
  <section class="video">
    <h2>VIDEO</h2>
    <div class="video-frame">
      <div class="video-screen" role="img" aria-label="Video player area">
        <svg width="62" height="62" viewBox="0 0 62 62"><circle cx="31" cy="31" r="28.5" fill="none" stroke="#fff" stroke-width="3.5"/><path d="M24 18 L44 31 L24 44 Z" fill="#fff"/></svg>
      </div>
    </div>
    <p>It is a long established fact that a reader will be distracted by the readable content of a page when looking at its layout. The point of using Lorem Ipsum is that it has a more-or-less normal distribution of letters, as opposed to using 'Content here, content here', making it look like readable English.</p>
    <a class="btn">READ MORE</a>
  </section>
</main>

<ul class="submenu programs-menu">
  <li>ACCOUNTING</li><li>ART</li><li>BIBLE</li><li>BUSINESS</li><li>CRIMINAL JUSTICE</li><li>DESIGN</li><li>EDUCATION</li><li>ENGINEERING</li><li>ENGLISH</li><li>LAW</li><li>LPN TO RN</li><li>MANAGEMENT</li><li>MATH</li><li>MBA</li><li>MPH</li><li>MEDICAL ASSISTING</li><li>MILITARY</li><li>NURSING</li><li>OCCUPATIONAL THERAPY</li><li>PARALEGAL</li><li>PSYCHOLOGY</li><li>PHARMACY</li><li>RN TO BSN</li><li>RADIOLOGY</li><li>SOCIAL WORK</li><li>SONOGRAPHY</li>
</ul>
<ul class="submenu degrees-menu">
  <li>CERTIFICATE</li><li>ASSOCIATE</li><li>BACHELORS</li><li>MASTERS</li><li>PHD</li>
</ul>

<footer>
  <div class="footer-links"><a>ABOUT US</a><span>|</span><a>PRIVACY</a></div>
  <div class="copyright">COPYRIGHT @ WWW.URL.COM</div>
</footer>

</body>
</html>
```